PAQ - 2025

Marlowe Works is a high precision CNC machining company which performs very technical work. Every year we have a theme which is a pillar that drives our production activity. Our theme for 2025 is PAQ
Productivity
Accountability
Quality
We will post these banners in our production areas and lobby.
PAQ should be in large bold orange letters. You can pull photos from my website www.marloweworks-mwi.example and my Instagram account Marlowe Works Inc.

```html
<!DOCTYPE html>
<html lang="en">
<head>
<meta charset="utf-8">
<title>PAQ-2025 Banner — Marlowe Works Inc.</title>
<link rel="stylesheet" href="https://fonts.googleapis.com/css2?family=Unbounded:wght@600;800&family=Roboto+Condensed:ital,wght@1,500&display=swap">
<style>
  :root {
    --stage: #323b46;
    --brand-blue: #0a6aab;
    --accent-orange: #f15a29;
    --ink-navy: #1b2a4a;
    --paper: #ffffff;
  }
  html, body {
    margin: 0;
    width: 1200px;
    height: 1200px;
    overflow: hidden;
    background: var(--stage);
  }
  .banner {
    position: absolute;
    left: 40px;
    top: 350px;
    width: 1120px;
    height: 472px;
    display: block;
  }
  .headline { font-family: "Unbounded", sans-serif; font-weight: 800; font-size: 52px; }
  .pillar { font-family: "Unbounded", sans-serif; font-weight: 800; font-size: 41px; fill: var(--paper); }
  .initial, .theme-code { fill: var(--accent-orange); }
  .theme-year { fill: var(--paper); }
  .brand-name { font-family: "Unbounded", sans-serif; font-weight: 600; font-size: 22px; fill: var(--ink-navy); }
  .tagline { font-family: "Roboto Condensed", sans-serif; font-style: italic; font-weight: 500; font-size: 7px; fill: var(--ink-navy); }
  .pillar-frame { fill: none; stroke: var(--paper); stroke-width: 2; }
  .leader { stroke: var(--paper); stroke-width: 2; }
</style>
</head>
<body>
<svg class="banner" viewBox="0 0 1120 472" xmlns="http://www.w3.org/2000/svg">
  <defs>
    <linearGradient id="machine-photo-tone" x1="0" y1="0" x2="1" y2="0">
      <stop offset="0" stop-color="#0a6aab" stop-opacity="0"/>
      <stop offset="0.25" stop-color="#3f80b0" stop-opacity="0.8"/>
      <stop offset="0.55" stop-color="#8c959d"/>
      <stop offset="0.8" stop-color="#6b6e72"/>
      <stop offset="1" stop-color="#b8b8b8"/>
    </linearGradient>
  </defs>

  <rect class="banner-base" width="1120" height="472" fill="var(--brand-blue)"/>

  <rect class="machine-photo" x="600" y="0" width="520" height="472" fill="url(#machine-photo-tone)"
        role="img" aria-label="Black-and-white close-up photo of CNC tool holders and a milling cutter in a collet chuck"/>

  <polygon class="logo-panel" points="0,0 512,0 456,118 0,118" fill="var(--paper)"/>

  <g class="brand-lockup">
    <text class="brand-name" x="100" y="66" textLength="290" lengthAdjust="spacingAndGlyphs">Marlowe Works Inc.</text>
    <circle cx="414" cy="58" r="13" fill="var(--ink-navy)"/>
    <text class="tagline" x="132" y="87" textLength="241" lengthAdjust="spacingAndGlyphs">"A complete CNC machining company" Swiss turning, 5 axis milling, CNC turning</text>
  </g>

  <text class="headline" x="122" y="184" textLength="384" lengthAdjust="spacingAndGlyphs"><tspan class="theme-code">PAQ-</tspan><tspan class="theme-year">2025</tspan></text>

  <g class="pillar-row">
    <line class="leader" x1="0" y1="243" x2="92" y2="243"/>
    <polygon class="pillar-frame" points="92,243 112,206 568,206 588,243 568,280 112,280"/>
    <text class="pillar" x="122" y="258" textLength="420" lengthAdjust="spacingAndGlyphs"><tspan class="initial">P</tspan>RODUCTIVITY</text>
  </g>

  <g class="pillar-row">
    <line class="leader" x1="0" y1="326" x2="92" y2="326"/>
    <polygon class="pillar-frame" points="92,326 112,289 632,289 652,326 632,362 112,362"/>
    <text class="pillar" x="124" y="340" textLength="494" lengthAdjust="spacingAndGlyphs"><tspan class="initial">A</tspan>CCOUNTABILITY</text>
  </g>

  <g class="pillar-row">
    <line class="leader" x1="0" y1="407" x2="92" y2="407"/>
    <polygon class="pillar-frame" points="92,407 112,370 406,370 426,407 406,444 112,444"/>
    <text class="pillar" x="122" y="422" textLength="244" lengthAdjust="spacingAndGlyphs"><tspan class="initial">Q</tspan>UALITY</text>
  </g>
</svg>
</body>
</html>
```